Disability and mental health support work company requires business card

Specialising
Wrenfield Disability is a new QCAP service aimed toward QCAP participants with a history of criminal justice, psychosocial/mental health, intellectual, and cognitive disabilities.

Our focus
Focusing on providing core QCAP supports for community participation, daily activities and supported independent living.

Authentic
Likeminded people wanting to make a difference in participant's lives.

Our aim to provide holistic and empowering supports targeted towards creating independence and guidance for all participants and families.
Over 35 years of experience working with people that have psychosocial, intellectual, and cognitive disabilities.

Industry/Entity Type

disability and mental health

Contact Information for Business Card

logo - business name

Colors
0054AA
0677BA
7BADD7
CADEEF
E8F1F8
FFF300
FFF600
FEFA6F
FFFEC7
FFFEE8

Requirements
Must have
• want double sided business cards(wont let me change it)
Should not have
• any disability related pictures

```html
<!DOCTYPE html>
<html lang="en">
<head>
<meta charset="utf-8">
<title>Wrenfield Disability – Business Card</title>
<link href="https://fonts.googleapis.com/css2?family=Arimo:wght@400;700&display=swap" rel="stylesheet">
<style>
  :root {
    --backdrop: #ebebea;
    --paper: #fbfbf9;
    --navy: #163a63;
    --sky: #7badd7;
    --gold: #e8a612;
    --edge: #d9a514;
    --ink: #4a4a4a;
    --rule: #a9a9a9;
  }
  * { box-sizing: border-box; margin: 0; padding: 0; }
  html, body { width: 1200px; height: 802px; overflow: hidden; }
  body {
    background: var(--backdrop);
    font-family: "Arimo", Arial, sans-serif;
    display: flex;
    align-items: center;
    justify-content: center;
    gap: 60px;
  }
  .card {
    width: 520px;
    height: 300px;
    position: relative;
    border-bottom: 4px solid var(--edge);
    border-right: 2px solid var(--edge);
    box-shadow: 0 6px 18px rgba(0,0,0,0.12);
  }
  /* Front */
  .card-front { background: var(--paper); display: flex; align-items: center; }
  .front-brand {
    width: 250px;
    display: flex;
    align-items: center;
    justify-content: center;
    gap: 12px;
  }
  .brand-dot {
    width: 46px; height: 46px; border-radius: 50%;
    background: var(--navy);
    flex: none;
  }
  .brand-name {
    font-weight: 700;
    font-size: 19px;
    line-height: 1.15;
    color: var(--navy);
  }
  .divider {
    width: 1px; height: 120px; background: var(--rule);
  }
  .front-details { padding-left: 22px; color: var(--ink); font-size: 13px; line-height: 1.3; }
  .person-name { color: var(--gold); font-weight: 700; font-size: 21px; line-height: 1.1; }
  .person-role { font-size: 13px; margin-bottom: 10px; }
  .address { margin-bottom: 10px; }
  .contact-list { list-style: none; }
  .contact-list li { display: flex; align-items: center; gap: 8px; }
  .contact-list svg { width: 12px; height: 12px; flex: none; }
  /* Back */
  .card-back {
    background: var(--navy);
    display: flex;
    align-items: center;
    justify-content: flex-end;
    padding-right: 48px;
  }
  .back-brand { display: flex; align-items: center; gap: 16px; }
  .brand-ring {
    width: 64px; height: 64px; border-radius: 50%;
    border: 2px solid var(--sky);
    flex: none;
  }
  .back-brand .brand-name { color: var(--sky); font-size: 24px; }
</style>
</head>
<body>
  <section class="card card-front" aria-label="Business card front">
    <div class="front-brand">
      <span class="brand-dot"></span>
      <span class="brand-name">Wrenfield<br>Disability</span>
    </div>
    <div class="divider"></div>
    <div class="front-details">
      <p class="person-name">Daniel Hartley</p>
      <p class="person-role">Manager</p>
      <p class="address">Your address, city<br>state, ZIP 0000</p>
      <ul class="contact-list">
        <li>
          <svg viewBox="0 0 12 12"><path d="M2.5 1 L4.5 1 L5 3.5 L3.8 4.4 Q5 7 7.6 8.2 L8.5 7 L11 7.5 L11 9.5 Q10.5 11 9 11 Q1 10 1 3 Q1 1.5 2.5 1 Z" fill="var(--gold)"/></svg>
          555-014-2100
        </li>
        <li>
          <svg viewBox="0 0 12 12"><rect x="1" y="2.5" width="10" height="7" fill="none" stroke="var(--gold)" stroke-width="1.2"/><path d="M1 2.5 L6 6.5 L11 2.5" fill="none" stroke="var(--gold)" stroke-width="1.2"/></svg>
          hello@wrenfieldmail.com
        </li>
        <li>
          <svg viewBox="0 0 12 12"><circle cx="6" cy="6" r="5" fill="var(--gold)"/><path d="M1 6 H11 M6 1 Q3 6 6 11 M6 1 Q9 6 6 11" fill="none" stroke="var(--paper)" stroke-width="0.8"/></svg>
          www.wrenfielddisability.com
        </li>
      </ul>
    </div>
  </section>

  <section class="card card-back" aria-label="Business card back">
    <div class="back-brand">
      <span class="brand-ring"></span>
      <span class="brand-name">Wrenfield<br>Disability</span>
    </div>
  </section>
</body>
</html>
```